BriMora Journeys Business Card Design

We need a new business card design for our travel agency business - BriMora Journeys. We design packages to some of the most popular travel destinations in the world for groups, individuals and also tailor-make personalised packages. Our logo attached must be used. On the back of the card we would like a list of all websites under our BriMora brand to be posted. We would like clean, modern, simple design.

Industry/Entity Type

Travel Agent

Contact Information for Business Card

Owen Farrant
National Sales Manager
Reservations: 1300 527 649
Tel: 61 28473 5961
Fax: 61 2847 3907
Email: owen@brimorajourneys.com.au
Web: www.brimorajourneys.com.au

Address: Level 1, 417 Harwood Street
Sydney NSW 2000 Australia

Requirements
Must have
• On the back of the card we want all websites listed under our BriMora brand.
• BriMora Journeys Group - Wholesale Specialists
• www.kpwander.com.au - New Caledonia
• www.islebreeze.com.au - Tahiti
• www.orientjourneyhub.com.au - China
Nice to have
• Modern, clean lined, simple and fresh
Should not have
• Look dull

```html
<!DOCTYPE html>
<html lang="en">
<head>
<meta charset="utf-8">
<title>BriMora Journeys Business Card</title>
<link href="https://fonts.googleapis.com/css2?family=Open+Sans:wght@400;600;700&display=swap" rel="stylesheet">
<style>
  :root {
    --navy: #1f2470;
    --card-blue: #34389a;
    --card-blue-light: #4a4fb0;
    --red: #e31d25;
    --white: #ffffff;
    --ink: #2b2b2b;
    --grey: #6a6a75;
    --stage: #2a2a2d;
  }
  * { margin: 0; padding: 0; box-sizing: border-box; }
  html, body { width: 1200px; height: 900px; overflow: hidden; }
  body {
    background: var(--stage);
    font-family: "Open Sans", Arial, sans-serif;
    position: relative;
  }
  .card {
    position: absolute;
    left: 280px;
    width: 640px;
    height: 365px;
    overflow: hidden;
    box-shadow: 0 14px 30px rgba(0,0,0,.45);
  }
  .card-back {
    top: 55px;
    background: linear-gradient(120deg, var(--card-blue) 0%, var(--card-blue-light) 100%);
    color: var(--white);
    text-align: center;
  }
  .card-back .brand-name {
    margin-top: 110px;
    font-size: 44px;
    font-weight: 700;
    letter-spacing: -0.5px;
    color: var(--white);
  }
  .site-list {
    list-style: none;
    margin-top: 18px;
    font-size: 15px;
    line-height: 24px;
    letter-spacing: 0.3px;
  }
  .card-front { top: 470px; background: var(--card-blue); }
  .card-front .shape { position: absolute; inset: 0; }
  .card-front .brand-name {
    position: absolute;
    top: 58px; left: 0; width: 100%;
    text-align: center;
    font-size: 38px;
    font-weight: 700;
    letter-spacing: -0.5px;
    color: var(--navy);
  }
  .person { position: absolute; left: 90px; top: 168px; }
  .person-name { font-size: 22px; font-weight: 700; color: var(--navy); line-height: 26px; }
  .person-title { font-size: 15px; color: var(--ink); }
  .contact-list { list-style: none; margin-top: 14px; }
  .contact-list li {
    display: flex; align-items: center; gap: 12px;
    font-size: 16px; line-height: 25px; color: var(--ink);
  }
  .contact-list li.web { color: var(--grey); }
  .contact-list svg { width: 14px; height: 14px; flex: none; }
  .details { position: absolute; left: 360px; top: 176px; list-style: none; }
  .details li {
    display: flex; align-items: flex-start; gap: 12px;
    font-size: 15px; line-height: 22px; color: var(--grey);
    margin-bottom: 4px;
  }
  .details svg { width: 14px; height: 14px; flex: none; margin-top: 4px; }
</style>
</head>
<body>

<section class="card card-back">
  <div class="brand-name">BriMora Journeys</div>
  <ul class="site-list">
    <li>www.kpwander.com.au - New Caledonia</li>
    <li>www.islebreeze.com.au - Tahiti</li>
    <li>www.orientjourneyhub.com.au - China</li>
  </ul>
</section>

<section class="card card-front">
  <svg class="shape" viewBox="0 0 640 365" aria-hidden="true">
    <ellipse cx="338" cy="186" rx="322" ry="196" fill="var(--red)"/>
    <ellipse cx="330" cy="194" rx="318" ry="196" fill="var(--white)"/>
    <ellipse cx="318" cy="210" rx="316" ry="196" fill="var(--white)"/>
  </svg>

  <div class="brand-name">BriMora Journeys</div>

  <div class="person">
    <div class="person-name">Owen Farrant</div>
    <div class="person-title">National Sales Manager</div>
    <ul class="contact-list">
      <li>
        <svg viewBox="0 0 16 16"><path fill="var(--navy)" d="M3.6 1.5l2.3 2.8-1.3 1.6c.9 2 2.4 3.6 4.5 4.6l1.6-1.3 2.8 2.3-1.5 2.4C7 13.6 2.4 9 1.2 3z"/></svg>
        61 28473 5961
      </li>
      <li>
        <svg viewBox="0 0 16 16"><rect x="1" y="3" width="14" height="11" rx="2" fill="var(--navy)"/><circle cx="10" cy="9" r="3" fill="var(--white)"/></svg>
        1300 527 649
      </li>
      <li>
        <svg viewBox="0 0 16 16"><rect x="4" y="1" width="8" height="5" fill="var(--navy)"/><rect x="1" y="6" width="14" height="9" rx="1" fill="var(--navy)"/><rect x="4" y="9" width="8" height="3" fill="var(--white)"/></svg>
        61 2847 3907
      </li>
      <li class="web">
        <svg viewBox="0 0 16 16" fill="none" stroke="var(--navy)" stroke-width="1.3"><circle cx="8" cy="8" r="6.5"/><ellipse cx="8" cy="8" rx="3" ry="6.5"/><path d="M1.5 8h13M2.5 4.8h11M2.5 11.2h11"/></svg>
        www.brimorajourneys.com.au
      </li>
    </ul>
  </div>

  <ul class="details">
    <li>
      <svg viewBox="0 0 16 16" fill="none" stroke="var(--navy)" stroke-width="1.8"><circle cx="8" cy="8" r="3"/><path d="M11 5v4.5c0 2 3 2 3-1.5A6 6 0 1 0 10.5 13.5"/></svg>
      owen@brimorajourneys.com.au
    </li>
    <li>
      <svg viewBox="0 0 16 16"><path fill="var(--navy)" d="M8 1a5 5 0 0 0-5 5c0 3.8 5 9 5 9s5-5.2 5-9a5 5 0 0 0-5-5z"/><circle cx="8" cy="6" r="1.8" fill="var(--white)"/></svg>
      <span>Level 1, 417 Harwood Street<br>Sydney NSW 2000 Australia</span>
    </li>
  </ul>
</section>

</body>
</html>
```